Telmoro Business Card

I already have the conplay logo. I need to develop a professional business card layout

Target Market(s)

Business

Industry/Entity Type

Business

Contact Information for Business Card

Company Name: Telmoro Limited

Font styles to use
Sans Serif

Colors

Designer to choose colors to be used in the design.

Requirements
Must have
• Use current logo
• Need two card size options:
• Small Card: 70mm x 28mm (Landscape)
• Square Card: 65mm x 65mm
Nice to have
• I will need 8-10 files for each name, number and email address (details to follow)

```html
<!DOCTYPE html>
<html lang="en">
<head>
<meta charset="utf-8">
<title>Telmoro Business Card – Size Options</title>
<link rel="stylesheet" href="https://fonts.googleapis.com/css2?family=Source+Sans+3:wght@400;600;700&display=swap">
<style>
  :root {
    --stage: #a7a7a7;
    --card: #e5e8e8;
    --ink: #2b2b2b;
    --label: #111111;
    --brand: #2e3192;
    --art-top: #d9457a;
    --art-mid: #6f6fc0;
    --art-low: #3fb4d8;
    --art-base: #5cb84a;
  }
  * { margin: 0; padding: 0; box-sizing: border-box; }
  html, body { width: 1200px; height: 1200px; overflow: hidden; }
  body {
    background: var(--stage);
    font-family: "Source Sans 3", "Segoe UI", Arial, sans-serif;
    position: relative;
    color: var(--ink);
  }
  .dimension {
    position: absolute;
    font-size: 31px;
    font-weight: 600;
    color: var(--label);
    line-height: 1;
  }
  .dimension--small-width { left: 62px; top: 20px; }
  .dimension--square-width { left: 509px; top: 222px; }
  .dimension--small-height {
    left: 22px; top: 1106px;
    transform: rotate(-90deg);
    transform-origin: left top;
  }
  .card {
    position: absolute;
    background: var(--card);
    overflow: hidden;
    box-shadow: 4px 6px 8px rgba(0,0,0,0.35);
  }
  .card--small { left: 62px; top: 60px; width: 418px; height: 1046px; }
  .card--square { left: 509px; top: 271px; width: 658px; height: 657px; }
  .card__art {
    position: absolute;
    background: linear-gradient(180deg, var(--art-top) 0%, var(--art-mid) 35%, var(--art-low) 68%, var(--art-base) 100%);
  }
  .card--small .card__art { left: 322px; top: 540px; width: 96px; height: 506px; }
  .card--square .card__art { left: 518px; top: 0; width: 140px; height: 657px; }
  .wordmark {
    position: absolute;
    font-weight: 700;
    color: var(--brand);
    line-height: 1;
    white-space: nowrap;
  }
  .card--small .wordmark { left: 44px; top: 166px; font-size: 74px; letter-spacing: 1px; }
  .card--square .wordmark { left: 44px; top: 108px; font-size: 102px; letter-spacing: 2px; }
  .fields { position: absolute; list-style: none; }
  .fields li { position: absolute; left: 0; white-space: nowrap; line-height: 1; }
  .card--small .fields { left: 43px; top: 0; font-size: 24px; }
  .card--small .fields li:nth-child(1) { top: 395px; }
  .card--small .fields li:nth-child(2) { top: 511px; }
  .card--small .fields li:nth-child(3) { top: 626px; }
  .card--small .fields li:nth-child(4) { top: 742px; }
  .card--square .fields { left: 46px; top: 0; font-size: 28px; }
  .card--square .fields li:nth-child(1) { top: 272px; }
  .card--square .fields li:nth-child(2) { top: 350px; }
  .card--square .fields li:nth-child(3) { top: 428px; }
  .card--square .fields li:nth-child(4) { top: 507px; }
</style>
</head>
<body>
  <div class="dimension dimension--small-width">28 mm</div>
  <div class="dimension dimension--square-width">65 mm</div>
  <div class="dimension dimension--small-height">70 mm</div>

  <section class="card card--small" aria-label="Small card, 70 by 28 mm">
    <div class="card__art" role="img" aria-label="Colourful faceted geometric artwork along the lower right edge"></div>
    <div class="wordmark">TELMORO</div>
    <ul class="fields">
      <li>Name:</li>
      <li>Address:</li>
      <li>Mobile:</li>
      <li>Email:</li>
    </ul>
  </section>

  <section class="card card--square" aria-label="Square card, 65 by 65 mm">
    <div class="card__art" role="img" aria-label="Colourful faceted geometric artwork along the right edge"></div>
    <div class="wordmark">TELMORO</div>
    <ul class="fields">
      <li>Name:</li>
      <li>Address:</li>
      <li>Mobile:</li>
      <li>Email:</li>
    </ul>
  </section>
</body>
</html>
```